Flyer Design - Spill Management Products - Selling to new clients

I am looking to produce an A4 double sided flyer. It is promoting our spill management products to prospective clients. This flyer is specifically targetting coal mines near where we operate.
I am not sure if I have provided too much text to fit in 2 pages, if so, I can reduce it if needed.
As it is selling to prospective clients, I think it needs to grab their attention. I basically want a bit of text, selling us and our company too them, and then feature a number of products.
If you need more clarification on what we want, please ask.
I would like it designed in InDesign if possible, as we have someone in house that could make changes to it when needed. I also intend to have this professionally printed.
You can view our company here – www.brantoveck.com.au
I have added a word document with details of what is to be included, plus the required images.
Cheers,
Oskar

```html
<!DOCTYPE html>
<html lang="en">
<head>
<meta charset="utf-8">
<title>Brantoveck – Spill Management Flyer</title>
<link href="https://fonts.googleapis.com/css2?family=Montserrat:wght@700;800&family=Questrial&display=swap" rel="stylesheet">
<style>
  :root {
    --backdrop: #ededed;
    --sheet-light: #a9a9ab;
    --sheet-mid: #8d8d90;
    --sheet-dark: #6e6e72;
    --ink: #1d1d1f;
    --ink-soft: #2a2a2c;
    --accent-yellow: #f2c21b;
    --accent-red: #d4261c;
    --tag-black: #0d0d0d;
    --rule: rgba(255,255,255,0.55);
    --white: #ffffff;
  }
  * { box-sizing: border-box; margin: 0; padding: 0; }
  html, body {
    width: 1200px; height: 936px; overflow: hidden;
    background: var(--backdrop);
  }
  body { position: relative; font-family: "Questrial", sans-serif; color: var(--ink); }

  .flyer {
    position: absolute; left: 288px; top: 28px;
    width: 624px; height: 880px; overflow: hidden;
    background: linear-gradient(160deg, var(--sheet-light) 0%, var(--sheet-mid) 45%, var(--sheet-dark) 100%);
    box-shadow: 0 6px 18px rgba(0,0,0,0.25);
  }
  .flyer-decor { position: absolute; inset: 0; width: 100%; height: 100%; }
  .flyer-content { position: relative; padding: 48px 44px 0 40px; }

  .brand { display: flex; align-items: center; justify-content: center; gap: 10px; margin-bottom: 22px; }
  .brand-mark { width: 26px; height: 26px; background: var(--ink); }
  .brand-name {
    font-family: "Montserrat", sans-serif; font-weight: 800;
    font-size: 26px; letter-spacing: 3px; color: var(--ink);
  }

  .headline {
    font-family: "Montserrat", sans-serif; font-weight: 800;
    font-size: 19px; line-height: 1.25; text-align: center;
    color: var(--ink); margin: 0 10px 26px;
  }

  .section { margin-bottom: 16px; font-size: 9.6px; line-height: 1.5; color: var(--ink-soft); }
  .section-title {
    font-family: "Montserrat", sans-serif; font-weight: 800;
    font-size: 12px; color: var(--accent-yellow); margin-bottom: 3px;
  }
  .section-title.red { color: var(--accent-red); }
  .bullets { list-style: none; padding-left: 8px; }
  .bullets li { position: relative; padding-left: 10px; }
  .bullets li::before { content: "•"; position: absolute; left: 0; }
  .sub-bullets { list-style: none; padding-left: 30px; }
  .sub-bullets li { position: relative; padding-left: 9px; }
  .sub-bullets li::before { content: "•"; position: absolute; left: 0; }
  .narrow { max-width: 340px; }

  .products-tag {
    display: inline-block; background: var(--tag-black); color: var(--accent-yellow);
    font-family: "Montserrat", sans-serif; font-weight: 800; font-size: 12px;
    padding: 4px 26px 4px 40px; margin: 4px 0 10px -40px;
  }

  .feature {
    position: absolute; right: 34px; top: 396px; width: 200px; height: 112px;
  }
  .feature-curl { position: absolute; inset: 0; width: 100%; height: 100%; }
  .feature-photo {
    position: absolute; right: 0; top: 0; width: 164px; height: 104px;
    background: var(--white); padding: 10px;
  }
  .feature-photo-fill {
    width: 100%; height: 100%;
    background: radial-gradient(ellipse at 45% 45%, #d9d9d9 0%, #a6a6a6 70%, #8a8a8a 100%);
  }
</style>
</head>
<body>
  <article class="flyer">
    <svg class="flyer-decor" viewBox="0 0 624 880" aria-hidden="true">
      <path d="M120 0 C 40 200, 60 520, 300 880" fill="none" stroke="rgba(255,255,255,0.35)" stroke-width="34"/>
      <line x1="0" y1="172" x2="624" y2="172" stroke="var(--rule)" stroke-width="1"/>
      <line x1="0" y1="254" x2="624" y2="254" stroke="var(--rule)" stroke-width="1"/>
      <line x1="0" y1="362" x2="624" y2="362" stroke="var(--rule)" stroke-width="1"/>
      <line x1="0" y1="484" x2="624" y2="484" stroke="var(--rule)" stroke-width="1"/>
      <line x1="0" y1="656" x2="624" y2="656" stroke="var(--rule)" stroke-width="1"/>
    </svg>

    <div class="flyer-content">
      <header class="brand">
        <span class="brand-mark"></span>
        <span class="brand-name">BRANTOVECK</span>
      </header>

      <h1 class="headline">Supplying quality spill management product to the mines in the Hunter Valley and NSW.</h1>

      <section class="section">
        <h2 class="section-title">About Us:</h2>
        <ul class="bullets">
          <li>Brantoveck is Newcastle's only owned and operated dedicated Spill Management Company.</li>
          <li>We currently supply some of the largest mines in NSW, and would like to supply you too.</li>
          <li>We only supply top quality products, to ensure they'll do the job you need.</li>
        </ul>
      </section>

      <section class="section">
        <h2 class="section-title">Benefits of Brantoveck:</h2>
        <ul class="bullets">
          <li>We manufacture and import products directly, so there is no middle man. This means the best price every time.</li>
          <li>We have a large Newcastle warehouse full of stock, meaning its always on hand when you need it.</li>
          <li>We'll deliver to your site.</li>
          <li>We can provide a service program, that includes restocking and usage reports.</li>
          <li>We've got every spill management product you'll ever need, we're your one stop shop.</li>
        </ul>
      </section>

      <section class="section narrow">
        <h2 class="section-title">Helping you change:</h2>
        <ul class="bullets">
          <li>We understand changing products and suppliers in the mining industry can be difficult.</li>
          <li>We'll assist by:</li>
        </ul>
        <ul class="sub-bullets">
          <li>Provide samples to conduct onsite testing</li>
          <li>Providing product performance details, datasheets and MSDS's</li>
          <li>Provide onsite training of our products</li>
        </ul>
      </section>

      <div class="products-tag">Products</div>

      <section class="section">
        <h2 class="section-title red">Spill Kits</h2>
        <ul class="bullets">
          <li>Spill kits are often the first line of defence on any site. It is important that you stock kits, that fit the task with quality products. We stock a wide range of spill kits in Oil Only, General Purpose and Hazchem. We also provide Spill Kit refills, to ensure you only order what you need.</li>
        </ul>
        <ul class="sub-bullets">
          <li>Feature this product</li>
          <li>100L General Purpose Spill Kit</li>
          <li>Photo uploaded also</li>
          <li>Add detail on what is included in the kit</li>
        </ul>
      </section>

      <section class="section">
        <h2 class="section-title red">Kit Contents</h2>
        <ul class="bullets">
          <li>1 x Red 240L wheelie bin</li>
          <li>1 x 10kg Brantoveck Organic Loose Absorbent</li>
          <li>50 x General Purpose Absorbent Pads</li>
          <li>5 x General Purpose Mini Booms (1.2m x 8cm)</li>
          <li>2 x General Purpose Grey Pillows (53cm x 46cm)</li>
          <li>1 x Small Pan/Brush</li>
          <li>2 x Kestrel PVC Gloves With Seamless Cotton Liner</li>
          <li>Consumables (as below)</li>
          <li>7 x Yellow Disposal Bags (Contaminated Waste Sign)</li>
          <li>7 x Cable Ties</li>
          <li>1 x Laminated Instruction Guide</li>
          <li>3 x Re-order Forms</li>
          <li>Safety Data Sheets</li>
        </ul>
      </section>
    </div>

    <figure class="feature">
      <svg class="feature-curl" viewBox="0 0 200 112" aria-hidden="true">
        <path d="M4 108 C 12 86, 28 76, 40 80 L 40 108 Z" fill="var(--accent-yellow)"/>
        <path d="M4 108 L 196 108 L 196 104 L 40 104 Z" fill="var(--accent-yellow)"/>
      </svg>
      <div class="feature-photo">
        <div class="feature-photo-fill" role="img" aria-label="Photo of the bagged 100L general purpose spill kit"></div>
      </div>
    </figure>
  </article>
</body>
</html>
```